Velmora Handel Stationary
Simple
Jonas Brückler
Co-Founder
Velmora Handel UG
Lindenkamp 12
48213 Heilbad Heiligenstadt
Germany
jonas.brueckler@velmora-handel.example
www.velmora-handel.example
Please use the some font as in the logo and work out a proposal based on the red and yellow logo in the uploaded rar file. Whether or not you use the globe in the back (you will see in the rar file) is up to you. The corporate slogan 'Your gateway to infinite opportunities' can be integrated but it's not a must.
Corporate Logo (with or without slogan, up to you)
Please refer to the logos. Ideally work sth out from the colorful version (red and yellow) with or without the globe in the back. You will see when looking at the file.

```html
<!DOCTYPE html>
<html lang="de">
<head>
<meta charset="utf-8">
<title>Velmora Handel Stationary</title>
<link href="https://fonts.googleapis.com/css2?family=Russo+One&family=Roboto:wght@400;700&display=swap" rel="stylesheet">
<style>
  :root {
    --red: #c8102e;
    --red-dark: #7a0a1c;
    --orange: #f28c1b;
    --yellow: #ffd23a;
    --paper: #ffffff;
    --ink: #4a4a4a;
    --rule: #bdbdbd;
    --bg: #ffffff;
  }
  * { box-sizing: border-box; margin: 0; padding: 0; }
  html, body { width: 1200px; height: 353px; overflow: hidden; background: var(--bg); }
  body { position: relative; font-family: "Roboto", Arial, sans-serif; color: var(--ink); }

  .sheet { position: absolute; background: var(--paper); box-shadow: 0 0 3px rgba(0,0,0,.35); overflow: hidden; }

  .footer-band { position: absolute; left: 0; right: 0; bottom: 0;
                 background: linear-gradient(180deg, var(--orange) 0%, var(--red) 45%, var(--red-dark) 100%); }

  .brand { position: absolute; display: flex; align-items: center; gap: 3px;
           font-family: "Russo One", Arial, sans-serif; color: var(--red); white-space: nowrap; line-height: 1; }
  .brand-dot { border-radius: 50%; background: var(--red); flex: none; }
  .brand.on-dark { color: var(--paper); }

  .info { position: absolute; font-size: 4px; line-height: 1.35; color: var(--ink); white-space: nowrap; }

  /* business cards */
  .card { left: 12px; width: 101px; height: 60px; }
  .card-red { background: linear-gradient(160deg, var(--red) 0%, var(--red-dark) 70%, var(--orange) 100%); }
  .card-orange { background: radial-gradient(circle at 60% 55%, var(--yellow), var(--orange) 55%, #e2571a); }
  .card .brand { font-size: 7px; }
  .card .brand-dot { width: 8px; height: 8px; }
  .card .brand.centered { left: 0; right: 0; justify-content: center; top: 26px; }

  /* letterheads */
  .letter { top: 12px; width: 246px; height: 331px; }
  .letter .brand { left: 14px; top: 16px; font-size: 10px; }
  .letter .brand-dot { width: 12px; height: 12px; }
  .letter .sender { right: 14px; top: 14px; text-align: right; }
  .letter .head-rule { position: absolute; left: 120px; right: 14px; top: 34px; height: 1px; background: var(--red); }
  .letter .footer-band { height: 46px; }

  /* envelopes */
  .env-back { left: 384px; top: 12px; width: 270px; height: 137px;
              background: linear-gradient(180deg, var(--red) 0%, var(--red-dark) 65%, var(--orange) 100%); }
  .env-back .brand { left: 0; right: 0; justify-content: center; top: 24px; font-size: 9px; }
  .env-front { left: 384px; top: 168px; width: 270px; height: 175px; }
  .env-front .brand { left: 14px; top: 30px; font-size: 10px; }
  .env-front .brand-dot { width: 12px; height: 12px; }
  .env-front .sender { left: 14px; top: 46px; }
  .env-front .footer-band { height: 40px; }

  /* fax form */
  .form-title { position: absolute; right: 14px; top: 44px; font-family: "Russo One", Arial, sans-serif;
                font-size: 7px; color: var(--paper); background: var(--red); padding: 2px 5px; }
  .form-fields { position: absolute; left: 14px; right: 14px; top: 62px; }
  .field { display: flex; align-items: flex-end; gap: 4px; height: 12px; font-size: 4.5px; }
  .field span { width: 22px; }
  .field i { flex: 1; border-bottom: 1px solid var(--rule); height: 1px; }
  .checks { position: absolute; left: 14px; right: 14px; top: 130px; display: flex; justify-content: space-between; font-size: 4px; }
  .checks label { display: flex; align-items: center; gap: 2px; }
  .checks label::before { content: ""; width: 4px; height: 4px; border: 0.6px solid var(--ink); }
</style>
</head>
<body>

<!-- business cards -->
<section class="sheet card" style="top:12px">
  <div class="brand" style="left:10px;top:8px"><span class="brand-dot"></span>VELMORA HANDEL</div>
  <div class="footer-band" style="height:14px" role="img" aria-label="Red and yellow decorative band"></div>
</section>
<section class="sheet card card-red" style="top:78px" role="img" aria-label="Red and yellow decorative card back">
  <div class="brand on-dark centered">VELMORA HANDEL</div>
</section>
<section class="sheet card" style="top:144px">
  <div class="brand" style="left:8px;top:7px"><span class="brand-dot"></span>VELMORA HANDEL</div>
  <div class="info" style="left:8px;top:22px">
    <b>Jonas Brückler</b><br>Co-Founder<br>Lindenkamp 12, 48213 Heilbad Heiligenstadt<br>jonas.brueckler@velmora-handel.example<br>www.velmora-handel.example
  </div>
</section>
<section class="sheet card card-red" style="top:210px">
  <div class="brand on-dark centered">VELMORA HANDEL</div>
</section>
<section class="sheet card card-orange" style="top:276px" role="img" aria-label="Orange and yellow decorative card back">
  <div class="brand centered">VELMORA</div>
</section>

<!-- letterhead -->
<section class="sheet letter" style="left:125px">
  <div class="brand"><span class="brand-dot"></span>VELMORA HANDEL</div>
  <div class="info sender">Velmora Handel UG · Lindenkamp 12<br>48213 Heilbad Heiligenstadt · Germany<br>www.velmora-handel.example</div>
  <span class="head-rule"></span>
  <div class="footer-band" role="img" aria-label="Red and yellow decorative band"></div>
</section>

<!-- envelope back -->
<section class="sheet env-back" role="img" aria-label="Red and yellow decorative envelope back">
  <div class="brand on-dark">VELMORA HANDEL</div>
</section>

<!-- envelope front -->
<section class="sheet env-front">
  <div class="brand"><span class="brand-dot"></span>VELMORA HANDEL</div>
  <div class="info sender">Velmora Handel UG · Lindenkamp 12 · 48213 Heilbad Heiligenstadt</div>
  <div class="footer-band" role="img" aria-label="Red and yellow decorative band"></div>
</section>

<!-- second letterhead -->
<section class="sheet letter" style="left:672px">
  <div class="brand"><span class="brand-dot"></span>VELMORA HANDEL</div>
  <div class="info sender">Velmora Handel UG · Lindenkamp 12<br>48213 Heilbad Heiligenstadt · Germany<br>www.velmora-handel.example</div>
  <div class="footer-band" role="img" aria-label="Red and yellow decorative band"></div>
</section>

<!-- fax form -->
<section class="sheet letter" style="left:929px">
  <div class="brand"><span class="brand-dot"></span>VELMORA HANDEL</div>
  <div class="info sender">Velmora Handel UG · Lindenkamp 12<br>48213 Heilbad Heiligenstadt · Germany<br>www.velmora-handel.example</div>
  <span class="head-rule"></span>
  <div class="form-title">FAX</div>
  <div class="form-fields">
    <div class="field"><span>Date</span><i></i></div>
    <div class="field"><span>To</span><i></i></div>
    <div class="field"><span>From</span><i></i></div>
    <div class="field"><span>Fax</span><i></i></div>
    <div class="field"><span>Subject</span><i></i></div>
  </div>
  <div class="checks">
    <label>Urgent</label><label>For Review</label><label>Please Reply</label><label>Please Comment</label>
  </div>
  <div class="footer-band" role="img" aria-label="Red and yellow decorative band"></div>
</section>

</body>
</html>
```